Business Card For Life Coaching Business For Men

Take my existing logo and apply it to a business card. I would like the logo to be prominent with stylistic text below reading Life Coaching For Men. Contact info should show as:
Gideon Marsh
gideon@bravepathgrowth.com

```html
<!DOCTYPE html>
<html lang="en">
<head>
<meta charset="UTF-8">
<title>Brave Path Growth – Business Card</title>
<link href="https://fonts.googleapis.com/css2?family=Montserrat:wght@400;500;600;700;800&display=swap" rel="stylesheet">
<style>
  :root {
    --page-bg: #3a3b3d;
    --card-white: #ffffff;
    --navy: #141b5e;
    --teal: #12908e;
    --steel: #7f9cc0;
    --ink: #1f2227;
  }
  * { margin: 0; padding: 0; box-sizing: border-box; }
  html, body {
    width: 1200px;
    height: 1200px;
    overflow: hidden;
    background: var(--page-bg);
    font-family: "Montserrat", sans-serif;
  }
  .sheet {
    position: relative;
    width: 1200px;
    height: 1200px;
  }
  .card {
    position: absolute;
    left: 150px;
    width: 900px;
    height: 514px;
    border-radius: 40px;
    overflow: hidden;
  }
  .card--front { top: 60px; background: var(--card-white); }
  .card--back  { top: 626px; background: var(--navy); }

  /* brand lockup */
  .brand {
    position: absolute;
    display: flex;
    align-items: center;
  }
  .brand__dot {
    border-radius: 50%;
    background: var(--teal);
    flex: none;
  }
  .brand__text { display: flex; flex-direction: column; }
  .brand__name {
    font-weight: 800;
    text-transform: uppercase;
    line-height: 1;
    letter-spacing: 0.01em;
  }
  .brand__tagline {
    font-weight: 700;
    text-transform: uppercase;
    letter-spacing: 0.06em;
  }

  .card--front .brand { top: 70px; left: 330px; gap: 22px; }
  .card--front .brand__dot { width: 96px; height: 96px; }
  .card--front .brand__name { font-size: 40px; color: var(--navy); }
  .card--front .brand__tagline { font-size: 15px; color: var(--ink); margin-top: 10px; }

  .card--back .brand { top: 150px; left: 150px; gap: 40px; }
  .card--back .brand__dot { width: 190px; height: 190px; }
  .card--back .brand__name { font-size: 58px; color: var(--card-white); }
  .card--back .brand__tagline { font-size: 22px; color: var(--card-white); margin-top: 16px; }

  .rule {
    position: absolute;
    height: 2px;
    background: var(--teal);
  }
  .rule--top { top: 238px; left: 240px; right: 60px; }
  .rule--mid { top: 400px; left: 70px; width: 360px; }

  .person {
    position: absolute;
    left: 70px;
    top: 320px;
  }
  .person__name {
    font-size: 38px;
    font-weight: 700;
    color: var(--teal);
    text-transform: uppercase;
    line-height: 1;
  }
  .person__role {
    font-size: 27px;
    font-weight: 500;
    color: var(--ink);
    letter-spacing: 0.04em;
    margin-top: 4px;
  }

  .contact {
    position: absolute;
    left: 70px;
    top: 418px;
    list-style: none;
  }
  .contact__item {
    display: flex;
    align-items: center;
    gap: 16px;
    font-size: 24px;
    color: var(--ink);
    letter-spacing: 0.03em;
    height: 40px;
  }
  .contact__icon { width: 26px; height: 26px; fill: var(--teal); flex: none; }
</style>
</head>
<body>
<main class="sheet">

  <section class="card card--front" aria-label="Business card front">
    <div class="brand">
      <span class="brand__dot"></span>
      <div class="brand__text">
        <span class="brand__name">Brave Path Growth</span>
        <span class="brand__tagline">Life Coaching For Men</span>
      </div>
    </div>

    <div class="rule rule--top"></div>

    <div class="person">
      <p class="person__name">Gideon Marsh</p>
      <p class="person__role">Life Coaching For Men</p>
    </div>

    <div class="rule rule--mid"></div>

    <ul class="contact">
      <li class="contact__item">
        <svg class="contact__icon" viewBox="0 0 24 24" aria-hidden="true"><path d="M6.6 10.8c1.4 2.8 3.8 5.1 6.6 6.6l2.2-2.2c.3-.3.7-.4 1-.2 1.1.4 2.3.6 3.6.6.6 0 1 .4 1 1V20c0 .6-.4 1-1 1C10.6 21 3 13.4 3 4c0-.6.4-1 1-1h3.5c.6 0 1 .4 1 1 0 1.3.2 2.5.6 3.6.1.3 0 .7-.2 1l-2.3 2.2z"/></svg>
        <span>(000) 000 0000</span>
      </li>
      <li class="contact__item">
        <svg class="contact__icon" viewBox="0 0 24 24" aria-hidden="true"><path d="M2 5h20v14H2z M3.5 6.5 12 13l8.5-6.5" fill="var(--teal)" stroke="#fff" stroke-width="1.4"/></svg>
        <span>gideon@bravepathgrowth.com</span>
      </li>
    </ul>
  </section>

  <section class="card card--back" aria-label="Business card back">
    <div class="brand">
      <span class="brand__dot"></span>
      <div class="brand__text">
        <span class="brand__name">Brave Path Growth</span>
        <span class="brand__tagline">Life Coaching For Men</span>
      </div>
    </div>
  </section>

</main>
</body>
</html>
```